Bright Path Therapies business cards and stationary

Need business cards and stationary designed to match previously made logo for for a new company based in Sydney NSW called 'Bright Path Therapies'.

We provide early intervention services and diagnostic assessment for children with disability and their families. I would like designs that are colourful and child friendly - possibly using feet/footprints/steps on a white background. The final design should communicate that we are family friendly, accepting and fun to work with.

Target Market(s)

Parents and Families
Teachers
Allied Health Professionals

Industry/Entity Type

Psychology

Contact Information for Business Card

Bright Path Therapies
www.brightpaththerapies-example.com
info@brightpaththerapies-example.com

Font styles to use
Sans Serif
Decorative
Script

Requirements
Must have
• Match the font and colour scheme of logo, along with footprint picture
Nice to have
• Clean and simple, while reflecting that I am working with families.
• Also- editable for when we make staff specific cards.

```html
<!DOCTYPE html>
<html lang="en">
<head>
<meta charset="utf-8">
<title>Bright Path Therapies – Business Card</title>
<link rel="stylesheet" href="https://fonts.googleapis.com/css2?family=Open+Sans:wght@600;700&family=Space+Mono&display=swap">
<style>
  :root {
    --card-white: #ffffff;
    --card-grey: #dedede;
    --fold-grey: #c9c9c9;
    --brand-red: #ee3f3a;
    --brand-blue: #1b75bb;
    --ink: #1a1a1a;
    --bubble-yellow: #e6ea3a;
    --bubble-green: #8cc63f;
    --bubble-deep: #4fb848;
  }
  html, body {
    margin: 0;
    width: 1200px;
    height: 686px;
    overflow: hidden;
    background: #ffffff;
  }
  .card {
    position: relative;
    width: 1200px;
    height: 686px;
    border-radius: 22px;
    overflow: hidden;
    background: linear-gradient(165deg, #ececec 0%, var(--card-white) 38%, var(--card-white) 100%);
    font-family: "Open Sans", Arial, sans-serif;
  }
  .card__decor {
    position: absolute;
    inset: 0;
  }
  .brand {
    position: absolute;
    left: 58px;
    top: 38px;
    display: flex;
    align-items: center;
    gap: 28px;
  }
  .brand__dot {
    width: 170px;
    height: 170px;
    border-radius: 50%;
    background: var(--brand-red);
  }
  .brand__name {
    margin: 0;
    font-weight: 700;
    font-size: 44px;
    color: var(--brand-blue);
    letter-spacing: 0.5px;
  }
  .contact {
    position: absolute;
    left: 106px;
    top: 474px;
  }
  .contact__heading {
    margin: 0;
    font-weight: 700;
    font-size: 37px;
    line-height: 48px;
    color: var(--brand-red);
  }
  .contact__company {
    margin: 0 0 6px;
    font-weight: 700;
    font-size: 31px;
    line-height: 42px;
    color: var(--brand-blue);
  }
  .contact__line {
    margin: 0;
    font-family: "Space Mono", "Courier New", monospace;
    font-size: 21px;
    line-height: 46px;
    letter-spacing: 5px;
    text-transform: uppercase;
    color: var(--ink);
  }
</style>
</head>
<body>
  <div class="card">
    <svg class="card__decor" width="1200" height="686" viewBox="0 0 1200 686">
      <defs>
        <linearGradient id="foldShade" x1="0" y1="0" x2="1" y2="1">
          <stop offset="0" stop-color="var(--fold-grey)" stop-opacity="0.55"/>
          <stop offset="0.6" stop-color="var(--card-grey)" stop-opacity="0.5"/>
          <stop offset="1" stop-color="var(--card-white)" stop-opacity="0"/>
        </linearGradient>
        <radialGradient id="bubbleGlow" cx="0.5" cy="0.5" r="0.5">
          <stop offset="0" stop-color="var(--bubble-deep)" stop-opacity="0.85"/>
          <stop offset="0.45" stop-color="var(--bubble-green)" stop-opacity="0.8"/>
          <stop offset="0.8" stop-color="var(--bubble-yellow)" stop-opacity="0.7"/>
          <stop offset="1" stop-color="var(--bubble-yellow)" stop-opacity="0"/>
        </radialGradient>
      </defs>
      <g role="img" aria-label="Soft grey page-curl swoosh with thin green lines along the left edge">
        <path d="M0,0 H1200 V30 C900,110 520,180 250,222 C150,238 110,300 96,400 C82,500 46,600 22,686 H0 Z" fill="url(#foldShade)"/>
      </g>
      <g role="img" aria-label="Cluster of translucent green and yellow bubbles in the lower right corner">
        <ellipse cx="1030" cy="470" rx="300" ry="320" fill="url(#bubbleGlow)"/>
      </g>
    </svg>

    <header class="brand">
      <div class="brand__dot"></div>
      <h1 class="brand__name">Bright Path Therapies</h1>
    </header>

    <section class="contact">
      <h2 class="contact__heading">Contact Information:</h2>
      <p class="contact__company">Bright Path Therapies</p>
      <p class="contact__line">www.brightpaththerapies-example.com</p>
      <p class="contact__line">info@brightpaththerapies-example.com</p>
    </section>
  </div>
</body>
</html>
```